social interest sharing site needs a web site design

we need a web site design for a social web platform.
the site is one page(main page), that is split into 3 sections
each section is a different color(red,green and blue)
and a user can choose to share each of the sections.
any section/color will contain boxes , each box can contain different media types.

the media types:
* list of URLS
* list of articles including title + image + description
* list of videos
* thumbnails of images
* calender
* list of emails

the main content will look like corkboardly layout
multiple boxes each box can contain different type of content as described above

each color is a different tab
each tab will have layout like corkboardly
Updates

please read the last description update.
and i uploaded an image that can explain the requirements better

thanks
Oren
 

Industry/Entity Type

Media

```html
<!DOCTYPE html>
<html lang="en">
<head>
<meta charset="utf-8">
<title>Hubnest — Social Interest Boards</title>
<link href="https://fonts.googleapis.com/css2?family=Didact+Gothic&family=Open+Sans:ital,wght@0,400;0,600;0,700;1,400&family=Arimo:wght@400;700&display=swap" rel="stylesheet">
<style>
  :root{
    --red:#9f130f;
    --red-dark:#8a0f0c;
    --green:#5aa92b;
    --blue:#0c3f7b;
    --blue-dark:#08315f;
    --blue-line:#2a5690;
    --white:#ffffff;
  }
  *{box-sizing:border-box;margin:0;padding:0}
  html,body{width:881px;height:1200px;overflow:hidden;background:var(--blue)}
  .page{position:relative;width:881px;height:1200px;overflow:hidden;font-family:"Open Sans",sans-serif;color:var(--white)}

  /* red section */
  .section-red{position:absolute;left:0;top:0;width:881px;height:436px;background:var(--red)}
  .topbar{position:absolute;left:0;top:0;width:881px;height:50px;border-bottom:1px solid var(--red-dark)}
  .brand-mark{position:absolute;left:92px;top:17px;width:14px;height:14px;background:var(--white)}
  .brand-name{position:absolute;left:113px;top:14px;font-family:"Didact Gothic",sans-serif;font-weight:400;font-size:16px;color:var(--white)}
  .nav{position:absolute;top:20px;left:515px;display:flex;gap:24px;font-family:"Didact Gothic",sans-serif;font-size:10.5px;letter-spacing:.3px}
  .nav-search{position:absolute;left:783px;top:22px}
  .section-title{position:absolute;left:0;width:881px;top:68px;text-align:center;font-family:"Didact Gothic",sans-serif;font-weight:400;font-size:22px;letter-spacing:-0.8px}
  .title-rule{position:absolute;top:106px;height:0;border-top:1px dotted rgba(255,255,255,.7)}
  .title-tag{position:absolute;top:101px;left:0;width:881px;text-align:center;font-family:"Arimo",sans-serif;font-size:7px;letter-spacing:.5px}
  .share-check{position:absolute;left:434px;top:127px}
  .url-card{position:absolute;top:156px;width:188px;height:198px;background:var(--white)}
  .url-card .shot{position:absolute;left:9px;top:8px;right:9px;bottom:8px}
  .url-caption{position:absolute;top:364px;width:200px;text-align:center;font-family:"Arimo",sans-serif;font-size:11.2px;line-height:13.5px;letter-spacing:-0.3px}
  .url-caption b{display:block;font-size:11px}
  .slider-arrow{position:absolute;top:240px;width:27px;height:27px;border:2px solid var(--white)}

  /* middle */
  .video-panel{position:absolute;left:0;top:436px;width:444px;height:364px;background:linear-gradient(160deg,#8e8f88 0%,#6d6c64 35%,#585850 55%,#6d8a45 85%,#5f7d3c 100%)}
  .video-play{position:absolute;left:195px;top:567px}
  .social-chip{position:absolute;top:449px;height:11px;padding:0 4px;font-family:"Arimo",sans-serif;font-size:7px;line-height:11px;color:#3b5a8c;background:#f2f4f8;border:1px solid #c4cad6;border-radius:2px}
  .social-count{position:absolute;top:449px;height:11px;padding:0 4px;font-family:"Arimo",sans-serif;font-size:7px;line-height:11px;color:#444;background:#fff;border:1px solid #c8c8c8;border-radius:2px}
  .section-green{position:absolute;left:444px;top:436px;width:437px;height:364px;background:var(--green)}
  .green-banner{position:absolute;left:452px;top:459px}
  .green-banner-text{position:absolute;left:470px;top:467px;font-size:16px;color:var(--green)}
  .thumb{position:absolute;width:169px;height:134px}
  .thumb-label{position:absolute;left:0;bottom:0;width:100%;height:26px;background:rgba(30,30,30,.78);font-size:11.5px;line-height:26px;padding-left:11px}

  /* blue */
  .section-blue{position:absolute;left:0;top:800px;width:881px;height:400px;background:var(--blue)}
  .col-divider{position:absolute;top:825px;width:1px;height:235px;background:rgba(255,255,255,.08)}
  .col-heading{position:absolute;top:845px;font-family:"Didact Gothic",sans-serif;font-weight:400;font-size:17px;letter-spacing:-1px}
  .article-thumb{position:absolute;left:88px;width:62px;height:53px}
  .article-title{position:absolute;left:158px;font-size:11.5px;font-weight:600}
  .article-meta{position:absolute;left:158px;font-size:9.5px;font-style:italic}
  .article-text{position:absolute;left:158px;font-size:9.5px;line-height:11px}
  .calendar{position:absolute;left:388px;top:884px;width:193px;height:119px;background:linear-gradient(180deg,#3a3f4a 0%,#5a5a66 40%,#6d6a68 70%,#4a3d34 100%);border:1px solid #2a3550}
  .cal-head{height:17px;background:#25292f;font-size:8px;font-weight:700;line-height:17px;padding-left:8px;position:relative}
  .cal-grid{display:grid;grid-template-columns:repeat(7,1fr);font-size:8.5px;text-align:center}
  .cal-grid span{height:16.8px;line-height:16.8px}
  .cal-grid .dow{font-weight:700;background:rgba(0,0,0,.45);height:17px;line-height:17px}
  .cal-grid .today{background:#1f74c8;font-weight:700}
  .cal-note{position:absolute;left:388px;top:1010px;font-size:8px;line-height:10px}
  .email-list{position:absolute;left:630px;top:885px;width:163px}
  .email-list div{height:17px;background:var(--blue-dark);border-bottom:1px solid var(--blue-line);font-size:8px;line-height:17px;padding-left:10px;color:#a9c4ea}
  .email-note{position:absolute;left:631px;top:968px;width:170px;font-size:8px;line-height:9.3px}
  .footer-rule{position:absolute;left:158px;top:1118px;width:563px;height:1px;background:rgba(255,255,255,.15)}
  .footer-text{position:absolute;left:0;width:881px;top:1136px;text-align:center;font-size:7.5px;color:#9fb5d6}
  .footer-social{position:absolute;left:0;width:881px;top:1155px;text-align:center;font-size:8px;color:#9fb5d6;font-weight:600}
  .to-top{position:absolute;left:793px;top:1177px;width:27px;height:23px}
</style>
</head>
<body>
<div class="page">

  <!-- Red: list of URLs -->
  <section class="section-red">
    <div class="topbar"></div>
    <div class="brand-mark"></div>
    <div class="brand-name">Hubnest</div>
    <nav class="nav"><span>HOME</span><span>WHAT WE DO</span><span>BLOGS</span><span>CONTACT</span></nav>
    <svg class="nav-search" width="10" height="10" viewBox="0 0 10 10" aria-hidden="true"><circle cx="4" cy="4" r="3" fill="none" stroke="#fff" stroke-width="1.4"/><line x1="6.2" y1="6.2" x2="9.3" y2="9.3" stroke="#fff" stroke-width="1.6"/></svg>

    <h1 class="section-title">LOREM IPSUM TEXT HEADING</h1>
    <div class="title-rule" style="left:283px;width:124px"></div>
    <div class="title-rule" style="left:474px;width:124px"></div>
    <div class="title-tag">[[ LIST OF URL ]]</div>
    <svg class="share-check" width="13" height="13" viewBox="0 0 13 13" aria-hidden="true"><rect x=".5" y=".5" width="12" height="12" fill="none" stroke="#fff"/><path d="M3 6.5L5.5 9L10.5 3" fill="none" stroke="#fff" stroke-width="1.3"/></svg>

    <div class="url-card" style="left:131px"><div class="shot" role="img" aria-label="Screenshot of a training courses website" style="background:linear-gradient(180deg,#e9ecef 0%,#cfd5da 40%,#72c6ea 48%,#72c6ea 58%,#f2f2f2 60%,#e4e4e4 100%)"></div></div>
    <div class="url-card" style="left:347px"><div class="shot" role="img" aria-label="Screenshot of a sports website" style="background:linear-gradient(180deg,#2b2b2b 0%,#4a4a4a 45%,#5b3030 60%,#476a3a 85%,#2d4a2a 100%)"></div></div>
    <div class="url-card" style="left:562px"><div class="shot" role="img" aria-label="Screenshot of a flower shop website" style="background:linear-gradient(180deg,#6b8c4a 0%,#f0e8e2 18%,#f6b24a 40%,#ffffff 46%,#f4f4f4 60%,#e88a2a 75%,#f5f5f5 100%)"></div></div>

    <div class="url-caption" style="left:125px"><b>www.samplecraft.net</b>In fermentum sit amet dolor non augue pretium egestas.</div>
    <div class="url-caption" style="left:341px"><b>www.samplecraft.net</b>In fermentum sit amet dolor non augue pretium egestas.</div>
    <div class="url-caption" style="left:556px"><b>www.samplecraft.net</b>In fermentum sit amet dolor non augue pretium egestas.</div>

    <svg class="slider-arrow" style="left:61px" viewBox="0 0 23 23" aria-hidden="true"><path d="M13.5 6.5L8.5 11.5L13.5 16.5" fill="none" stroke="#fff" stroke-width="2.4"/></svg>
    <svg class="slider-arrow" style="left:793px" viewBox="0 0 23 23" aria-hidden="true"><path d="M9.5 6.5L14.5 11.5L9.5 16.5" fill="none" stroke="#fff" stroke-width="2.4"/></svg>
  </section>

  <!-- Video -->
  <div class="video-panel" role="img" aria-label="Video still of two women working on laptops outdoors"></div>
  <svg class="video-play" width="62" height="62" viewBox="0 0 62 62" aria-hidden="true"><circle cx="31" cy="31" r="31" fill="#1d1d1d" opacity=".9"/><path d="M25 20L42 31L25 42Z" fill="#fff"/></svg>
  <div class="social-chip" style="left:316px">Like</div>
  <div class="social-count" style="left:355px">61</div>
  <div class="social-chip" style="left:377px">Share</div>
  <div class="social-count" style="left:414px">101</div>

  <!-- Green: image thumbnails -->
  <section class="section-green"></section>
  <svg class="green-banner" width="341" height="38" viewBox="0 0 341 38" aria-hidden="true"><path d="M0 0H341L331 19L341 38H0Z" fill="#fff"/></svg>
  <div class="green-banner-text">Lorem Ipsum Text Heading</div>

  <div class="thumb" style="left:450px;top:516px;background:linear-gradient(135deg,#b9a58a,#4a4b52 60%,#2d3038)" role="img" aria-label="Photo of smiling business people"><div class="thumb-label">Lorem Ipsum Text</div></div>
  <div class="thumb" style="left:624px;top:516px;background:linear-gradient(160deg,#d9dde0,#9aa2a8 55%,#3f4348)" role="img" aria-label="Photo of a team meeting in an office"><div class="thumb-label">Lorem Ipsum Text</div></div>
  <div class="thumb" style="left:450px;top:658px;background:linear-gradient(160deg,#c9d2dc,#6a7590 45%,#1c2a6e 80%)" role="img" aria-label="Photo of a conference table with red chairs"><div class="thumb-label">Lorem Ipsum Text</div></div>
  <div class="thumb" style="left:624px;top:658px;background:linear-gradient(160deg,#f2f2f2,#d8d8d8 50%,#5a4a40)" role="img" aria-label="Photo of a woman working at a laptop"><div class="thumb-label">Lorem Ipsum Text</div></div>

  <!-- Blue: articles, calendar, emails -->
  <section class="section-blue"></section>
  <div class="col-divider" style="left:362px"></div>
  <div class="col-divider" style="left:605px"></div>

  <h2 class="col-heading" style="left:87px">LIST OF ARTICLES</h2>
  <h2 class="col-heading" style="left:387px">CALENDER</h2>
  <h2 class="col-heading" style="left:633px">LIST OF EMAILS</h2>

  <div class="article-thumb" style="top:882px;background:linear-gradient(90deg,#2a2f3a,#5c4f4a 60%,#b8907a)" role="img" aria-label="Article thumbnail photo"></div>
  <div class="article-title" style="top:881px">Lorem artocle text lorem ipsum..</div>
  <div class="article-meta" style="top:898px">Posted on 18 Dec 2013</div>
  <div class="article-text" style="top:912px">Lorem ipsum dolor sit amet, consectetur<br>adipisicing elit, sed do eiusmod...</div>

  <div class="article-thumb" style="top:960px;background:linear-gradient(90deg,#2a2f3a,#5c4f4a 60%,#b8907a)" role="img" aria-label="Article thumbnail photo"></div>
  <div class="article-title" style="top:960px">Lorem artocle text lorem ipsum..</div>
  <div class="article-meta" style="top:977px">Posted on 18 Dec 2013</div>
  <div class="article-text" style="top:991px">Lorem ipsum dolor sit amet, consectetur<br>adipisicing elit, sed do eiusmod...</div>

  <div class="calendar">
    <div class="cal-head">DECEMBER &nbsp;– 2013
      <svg style="position:absolute;right:5px;top:3px" width="11" height="11" viewBox="0 0 11 11" aria-hidden="true"><rect x=".5" y="1.5" width="10" height="9" fill="#bbb"/><rect x=".5" y="1.5" width="10" height="2.5" fill="#888"/></svg>
    </div>
    <div class="cal-grid">
      <span class="dow">M</span><span class="dow">T</span><span class="dow">W</span><span class="dow">T</span><span class="dow">F</span><span class="dow">S</span><span class="dow">S</span>
      <span></span><span></span><span></span><span>1</span><span>2</span><span>3</span><span>4</span>
      <span>5</span><span>6</span><span>7</span><span>8</span><span>9</span><span>10</span><span>11</span>
      <span>12</span><span>13</span><span>14</span><span>15</span><span class="today">16</span><span>17</span><span>18</span>
      <span>19</span><span>20</span><span>21</span><span>22</span><span>23</span><span>24</span><span>25</span>
      <span>26</span><span>27</span><span>28</span><span>29</span><span>30</span><span>31</span><span></span>
    </div>
  </div>
  <div class="cal-note">Lorem ipsum dolor sit amet, consectetur elit sed<br>adipisicing elit, sed do</div>

  <div class="email-list">
    <div>support@hubnestmail.com</div>
    <div>loremipsum@hubnestmail.com</div>
    <div>support@hubnestmail.com</div>
    <div>loremipsum@hubnestmail.com</div>
  </div>
  <p class="email-note">Lorem ipsum dolor sit amet, consectetur adipisicing elit, sed do eiusmod Lorem ipsum dolor sit amet, consectetur adipisicing elit, sed do eiusmod</p>

  <div class="footer-rule"></div>
  <div class="footer-text">All Right Reserved © 2014 &nbsp;With Hubnest</div>
  <div class="footer-social">Linkly &nbsp; Chirp</div>
  <svg class="to-top" viewBox="0 0 27 23" aria-hidden="true"><rect width="27" height="23" fill="#fff"/><path d="M8 14L13.5 8.5L19 14" fill="none" stroke="#0c3f7b" stroke-width="3"/></svg>

</div>
</body>
</html>
```